Business Card Design Project

We need a business card design for a new company based in Singapore called 'Bright Ladder Pte Ltd'. We provide personal development training and emotional intelligence workshops. Our slogan is "Climb to your best self". We will not have a company address on the business card. Only phone number, email address and website address.

Target Market(s)

Adults age 25 to 45 years old.
Mostly working in a job.

Industry/Entity Type

Training

Colors
0255a2
f37123

```html
<!DOCTYPE html>
<html lang="en">
<head>
<meta charset="utf-8">
<title>Bright Ladder Pte Ltd — Business Card</title>
<link href="https://fonts.googleapis.com/css2?family=Open+Sans:wght@400;600;700&display=swap" rel="stylesheet">
<style>
  :root {
    --navy: #0255a2;
    --navy-deep: #1c2f6b;
    --orange: #f37123;
    --ink: #2b2b2b;
    --grey: #9a9a9a;
    --card: #ffffff;
    --backdrop: #e8e9eb;
  }
  * { box-sizing: border-box; margin: 0; padding: 0; }
  html, body { width: 1200px; height: 675px; overflow: hidden; }
  body {
    background: var(--backdrop);
    font-family: "Open Sans", Arial, sans-serif;
    position: relative;
  }
  .card {
    position: absolute;
    top: 195px;
    width: 500px;
    height: 286px;
    background: var(--card);
    box-shadow: 0 6px 18px rgba(0,0,0,0.12);
    overflow: hidden;
  }
  .card--front { left: 70px; }
  .card--back { left: 630px; }

  .brand { display: flex; align-items: center; gap: 12px; }
  .brand__dot { border-radius: 50%; border: 5px solid var(--navy-deep); flex: none; }
  .brand__name { color: var(--navy-deep); font-weight: 700; white-space: nowrap; line-height: 1; }

  .card--front .brand {
    position: absolute; left: 0; right: 0; top: 112px; justify-content: center;
  }
  .card--front .brand__dot { width: 52px; height: 52px; }
  .card--front .brand__name { font-size: 27px; }
  .front-rule {
    position: absolute; left: 150px; width: 210px; top: 175px;
    height: 1px; background: var(--grey);
  }

  .edge-bar { position: absolute; width: 6px; height: 44px; background: var(--orange); }
  .edge-bar--top { right: 0; top: 18px; }
  .edge-bar--bottom { left: 0; bottom: 18px; }
  .top-rule { position: absolute; left: 280px; right: 0; top: 70px; height: 1px; background: var(--orange); }

  .card--back .brand { position: absolute; left: 22px; top: 118px; gap: 8px; }
  .card--back .brand__dot { width: 32px; height: 32px; border-width: 3px; }
  .card--back .brand__name { font-size: 14px; }
  .tagline {
    position: absolute; left: 62px; top: 142px;
    font-size: 8.5px; color: var(--ink); letter-spacing: 0.2px;
  }

  .person { position: absolute; left: 272px; top: 108px; width: 200px; }
  .person__name { color: var(--navy-deep); font-size: 15px; font-weight: 700; }
  .person__title { font-size: 8px; color: var(--ink); margin-top: 2px; }
  .person__rule { height: 1px; background: var(--orange); margin-top: 6px; }

  .contacts { list-style: none; margin-top: 14px; }
  .contacts li {
    display: flex; align-items: center; gap: 10px;
    font-size: 11px; color: var(--ink); height: 20px;
  }
  .contacts svg { width: 11px; height: 11px; fill: var(--navy-deep); flex: none; }
</style>
</head>
<body>

  <section class="card card--front" aria-label="Card front">
    <div class="brand">
      <span class="brand__dot"></span>
      <span class="brand__name">Bright Ladder Pte Ltd</span>
    </div>
    <div class="front-rule"></div>
  </section>

  <section class="card card--back" aria-label="Card back">
    <div class="edge-bar edge-bar--top"></div>
    <div class="top-rule"></div>
    <div class="edge-bar edge-bar--bottom"></div>

    <div class="brand">
      <span class="brand__dot"></span>
      <span class="brand__name">Bright Ladder Pte Ltd</span>
    </div>
    <p class="tagline">Climb to your best self</p>

    <div class="person">
      <h1 class="person__name">Your Name</h1>
      <p class="person__title">Title</p>
      <div class="person__rule"></div>
      <ul class="contacts">
        <li>
          <svg viewBox="0 0 24 24" aria-hidden="true"><path d="M6.6 10.8a15.5 15.5 0 0 0 6.6 6.6l2.2-2.2c.3-.3.7-.4 1-.2 1.1.4 2.3.6 3.6.6.6 0 1 .4 1 1V20c0 .6-.4 1-1 1A17 17 0 0 1 3 4c0-.6.4-1 1-1h3.5c.6 0 1 .4 1 1 0 1.3.2 2.5.6 3.6.1.3 0 .7-.2 1z"/></svg>
          00.00.00.0000
        </li>
        <li>
          <svg viewBox="0 0 24 24" aria-hidden="true"><path d="M2 5h20v14H2z M2 5l10 8 10-8" fill="none" stroke="#1c2f6b" stroke-width="3"/></svg>
          yourname@yourwebsite.com
        </li>
        <li>
          <svg viewBox="0 0 24 24" aria-hidden="true"><circle cx="12" cy="12" r="10" fill="none" stroke="#1c2f6b" stroke-width="2.5"/><path d="M2 12h20M12 2c3 3 3 17 0 20M12 2c-3 3-3 17 0 20" fill="none" stroke="#1c2f6b" stroke-width="2"/></svg>
          www.yourwebsite.com
        </li>
      </ul>
    </div>
  </section>

</body>
</html>
```